Refresh look of our invoices (Excel spreadsheet which converts to PDF) to better match our new look

We have recently updated our Website and other marketing material with a new look and would like to refresh our invoice template so that it better matches our new look.  The template is an excel spreadsheet which we convert to a PDF to send out to our clients.
The main requirement is to incorporate the newer design colours and general look/feel to align with what is on our website www.corvalhill.com.au
It is extremely important that excel formula functionality and general layout are much the same although we are open to any design suggestions you might have.
Please note:
-Totals figures and news panel must remain on the first page
-We need full ability to edit embedded formulas and Excel spreadsheet is NOT to be password protected as we will only be using it internally.
-It is crucial that the second and subsequent pages can be extended (duplicated) internally to allow for larger multi page entries. Some of our clients invoices run up to 4/5 pages in length and we need the abilty to keep adding rows)
-possibility to add a "convert to PDF" button within the sheet which provides a 1 click solution to convert to PDF rather than the manual 2 step process to convert.... If that can be done, we would not want the "convert to PDF" button to show on final PDF converted version we issue to our customers.   Ideally, a single "convert to PDF and print first cover page only" in 1 single click button named 'convert to PDF & print' would be really handy.  -  (Just to explain why - we email out a PDF version of invoice to our clients and only print off first page with totals for our records)
The design for the first page can be different from the second & subsequent pages (eg first page can be more fancy with following pages more basic)

Finance Industry
Marketing

```html
<!DOCTYPE html>
<html lang="en">
<head>
<meta charset="utf-8">
<title>Recipient Created Tax Invoice</title>
<link href="https://fonts.googleapis.com/css2?family=Arimo:wght@400;700&display=swap" rel="stylesheet">
<style>
:root{
  --brand-green:#7dc42a;
  --brand-ink:#2b2b2b;
  --title-bar:#595959;
  --row-shade:#f2f2f2;
  --row-plain:#ffffff;
  --rule:#d9d9d9;
  --rule-dark:#a6a6a6;
  --news-band:#c4d79b;
  --alert-red:#ff0000;
  --link-blue:#0000ee;
  --text:#111111;
}
*{box-sizing:border-box;margin:0;padding:0}
html,body{width:1200px;height:1000px;overflow:hidden;background:#fff}
body{font-family:"Arimo",Arial,sans-serif;color:var(--text);position:relative}
.brand-block{position:absolute;left:208px;top:226px;width:228px;height:49px;background:var(--brand-green);
  display:flex;align-items:center;padding-left:12px;}
.brand-name{font-size:26px;font-weight:700;color:var(--brand-ink);letter-spacing:1px}
.company-contact{position:absolute;right:214px;top:221px;text-align:right;font-size:11px;line-height:14px}
.company-contact .sep{margin:0 6px}
.contact-rule{position:absolute;left:436px;top:254px;width:550px;height:1px;background:var(--rule)}
.company-abn{position:absolute;right:214px;top:257px;font-size:13px;font-weight:700;letter-spacing:.5px}
.header-rule{position:absolute;left:208px;top:276px;width:780px;height:3px;background:var(--rule)}
.invoice{position:absolute;left:208px;top:294px;width:780px;border:1px solid var(--rule-dark);border-top:none}
.invoice-title{height:29px;background:var(--title-bar);color:#fff;font-weight:700;font-size:15px;
  display:flex;align-items:center;justify-content:center}
.row{position:relative;border-bottom:1px solid #e4e4e4;font-size:12px;display:flex;align-items:center}
.row.shade{background:var(--row-shade)}
.row .label{width:149px;padding-left:13px;border-right:1px solid #e4e4e4;height:100%;display:flex;align-items:center}
.row .value{padding-left:3px}
.bold{font-weight:700}
.date-label{position:absolute;left:557px;width:94px;height:100%;border-left:1px solid #e4e4e4;border-right:1px solid #e4e4e4;
  display:flex;align-items:center;justify-content:center;font-weight:700}
.date-value{position:absolute;right:2px;font-weight:700}
.sum-label{position:absolute;right:141px}
.sum-value{position:absolute;left:650px;width:128px;height:100%;border-left:1px solid #e4e4e4;display:flex;align-items:center;justify-content:flex-end;padding-right:2px}
.negative{color:var(--alert-red)}
.news-band{height:26px;background:var(--news-band);color:var(--alert-red);font-weight:700;font-size:12px;
  display:flex;align-items:center;padding-left:13px;border-bottom:1px solid #e4e4e4}
.news-body{background:var(--row-shade);font-size:11px;line-height:15px;padding:8px 13px 9px}
.news-body a{color:var(--link-blue);text-decoration:none}
.footer-rule{position:absolute;left:208px;top:707px;width:780px;height:3px;background:#8c8c8c}
.footer-note{position:absolute;left:208px;top:714px;width:780px;text-align:center;font-size:10.5px;line-height:13px}
</style>
</head>
<body>
  <div class="brand-block"><span class="brand-name">CORVAL HILL</span></div>
  <div class="company-contact">
    Corval Hill Pty Ltd, Level 12, 85 Harlow Street, Melbourne Vic 3000<br>
    Ph (1300) 555 014<span class="sep">|</span>Fax (1300) 555 028<span class="sep">|</span>www.corvalhill.com.au
  </div>
  <div class="contact-rule"></div>
  <div class="company-abn">ABN&nbsp; 48 203 611 975</div>
  <div class="header-rule"></div>

  <section class="invoice">
    <div class="invoice-title">RECIPIENT CREATED TAX INVOICE</div>
    <div class="row" style="height:22px"></div>
    <div class="row shade" style="height:17px"><div class="label">Referer Name</div><div class="value bold">Arjun Prakash Menon</div></div>
    <div class="row" style="height:17px"></div>
    <div class="row shade" style="height:17px"><div class="label">Referer Address</div><div class="value">T C 12/508-3, Kovil Street</div></div>
    <div class="row" style="height:16px"><div class="label"></div><div class="value">Marinagar P O, Kollamkara</div></div>
    <div class="row shade" style="height:17px"><div class="label"></div></div>
    <div class="row" style="height:16px"></div>
    <div class="row shade" style="height:19px"><div class="label bold">Referer ABN</div><div class="value bold">00 000 000 000</div>
      <div class="date-label">Invoice Date</div><div class="date-value">18-Sep-13</div></div>
    <div class="row" style="height:19px"></div>
    <div class="row shade" style="height:17px"><span class="sum-label">Upfront</span><span class="sum-value">$4,000.00</span></div>
    <div class="row" style="height:16px"><span class="sum-label">Trail</span><span class="sum-value">$202.26</span></div>
    <div class="row shade" style="height:17px"><span class="sum-label">Adjustments</span><span class="sum-value negative">-$50.00</span></div>
    <div class="row" style="height:16px"><span class="sum-label">GST</span><span class="sum-value">$315.24</span></div>
    <div class="row shade" style="height:17px"><span class="sum-label bold">Total Amount Deposited</span><span class="sum-value bold">$4,467.50</span></div>
    <div class="row" style="height:19px"></div>
    <div class="news-band">***CORVAL LINK - Referral management software***</div>
    <div class="news-body">The Corval Link software provides you with a fully compliant referral process that is supported by the lenders. Apart from making new referrals, you can also read lender updates on deal progress and lodge enquires for outstanding commission payments. You can login by going to the dedicated Corval Link website at: <a href="#">www.corvalmembers.com.au</a></div>
  </section>

  <div class="footer-rule"></div>
  <p class="footer-note">This report contains confidential client information. Disclosure of customer information such as loan details and lenders to third parties may be a contravention of the Privacy Act, unless they are authorised to receive such details.</p>
</body>
</html>
```